Business Card Design- Mortgage Firm

Looking to design a business Card for our Outside sales people. This card is used to provide their contact information to prospective clients and realtors. Must have All Pertinent company and licensing information by law. We are looking for a very modern design that flows with our current logo color scheme. Red/White/Black

Industry/Entity Type

Mortgage Lender

Contact Information for Business Card

Must stick with current color scheme.

Colors
f04a50
ffffff
ecf7fb

Requirements
Must have
• Company Logo or similar
• Company Address (748 W Alder Avenue, Suite 312, Corona CA 92879 NMLS: 4072916)
• Agent Name (Mira Talbot)
• Title (Senior Mortgage Loan Originator)
• NMLS# 8395021
• Toll Free: 800-627-3184
• Direct : 310-555-4860
Nice to have
• Room for Agent Picture

```html
<!DOCTYPE html>
<html lang="en">
<head>
<meta charset="utf-8">
<title>Halvern Mortgage – Business Card</title>
<link href="https://fonts.googleapis.com/css2?family=Lato:wght@400;700&family=Montserrat:wght@600&display=swap" rel="stylesheet">
<style>
  :root {
    --backdrop: #3a3532;
    --card: #121212;
    --card-edge: #1c1c1c;
    --red: #d3262d;
    --white: #ffffff;
    --silver: #d6d6d6;
    --muted: #9a9a9a;
    --divider: #4a4a4a;
  }
  * { margin: 0; padding: 0; box-sizing: border-box; }
  html, body {
    width: 1200px; height: 900px; overflow: hidden;
    background: var(--backdrop);
    font-family: "Lato", sans-serif;
  }
  .canvas {
    position: relative; width: 1200px; height: 900px;
    display: flex; align-items: center; justify-content: center; gap: 50px;
  }
  .card {
    width: 525px; height: 300px;
    background: var(--card);
    border: 1px solid var(--card-edge);
    box-shadow: 0 14px 30px rgba(0,0,0,.45);
    position: relative;
    overflow: hidden;
  }

  /* Front: agent details */
  .card-front { display: flex; align-items: center; }
  .front-brand {
    width: 220px; display: flex; align-items: center; justify-content: center; gap: 10px;
  }
  .brand-mark { width: 16px; height: 16px; background: var(--red); flex: none; }
  .front-brand .brand-name {
    font-family: "Lato", sans-serif; font-weight: 700;
    font-size: 21px; color: var(--red); letter-spacing: .5px; line-height: 1.15;
  }
  .front-divider { width: 1px; height: 150px; background: var(--divider); }
  .agent {
    padding-left: 26px; color: var(--white); font-size: 15px; line-height: 1.3;
  }
  .agent-name { color: var(--red); font-weight: 700; font-size: 17px; text-transform: uppercase; }
  .agent-title { margin-bottom: 12px; }
  .contact-label { color: var(--red); }
  .agent-phones { margin-bottom: 12px; }
  .agent-address { font-style: normal; }

  /* Back: company */
  .card-back {
    display: flex; flex-direction: column; align-items: center; justify-content: center; gap: 26px;
  }
  .back-brand { display: flex; align-items: center; gap: 14px; }
  .back-brand .brand-mark { width: 24px; height: 24px; background: var(--silver); }
  .back-brand .brand-name {
    font-family: "Montserrat", sans-serif; font-weight: 600;
    font-size: 28px; letter-spacing: 3px; color: var(--silver); text-transform: uppercase;
    white-space: nowrap;
  }
  .licensing { color: var(--silver); font-size: 13px; letter-spacing: .5px; }
  .licensing .sep { margin: 0 12px; color: var(--muted); }
</style>
</head>
<body>
<main class="canvas">
  <section class="card card-front" aria-label="Business card front">
    <div class="front-brand">
      <span class="brand-mark" aria-hidden="true"></span>
      <span class="brand-name">Halvern<br>Mortgage</span>
    </div>
    <div class="front-divider" aria-hidden="true"></div>
    <div class="agent">
      <p class="agent-name">Mira Talbot</p>
      <p class="agent-title">Senior Mortgage Loan Originator</p>
      <div class="agent-phones">
        <p><span class="contact-label">Toll Free:</span> 800-627-3184</p>
        <p><span class="contact-label">Direct :</span> 310-555-4860</p>
      </div>
      <address class="agent-address">
        748 W Alder Avenue, Suite 312<br>Brenmoor CA 92879
      </address>
    </div>
  </section>

  <section class="card card-back" aria-label="Business card back">
    <div class="back-brand">
      <span class="brand-mark" aria-hidden="true"></span>
      <span class="brand-name">Halvern Mortgage</span>
    </div>
    <p class="licensing">NMLS: 4072916<span class="sep">|</span>NMLS# 8395021</p>
  </section>
</main>
</body>
</html>
```